Background on the company
=======================
This is a Bitcoin Consulting Company.

We have two projects.

Tinted Tokens: software to trade assets over the Bitcoin protocol (assets like property, traditional currencies, gold, stocks, securities, bonds, etc.).

Vaultrix Home Teller: a hardware based web service in a box that manages cold storage wallets and off line transaction signing. It is the secure way to deploy a web wallet without relying on third parties.

All that to say this is a high tech company focusing on Bitcoin.

What does Drellowmar mean?
========================

The Beast of Drellowmar is the rabbit in Quimby Larkets's Silver Goblet that defeats his band of knights. (At least until they go and get the Holy Hand Grenade).

We like this, because we are a deceptively soft and fuzzy company that is also killer!

What We Need:
============

Primarily we need to get the logo designed. I have a hand drawing I did, but you are not limited to that. And the logo needs to work on a business card. The right logo that works on a Business Card is the primary consideration.
Updates

The main task here is to get the logo right.  I have provided a drawing I made, and I like it, but my complaints are:  Drellowmar is hard to read.  The 'C' isn't obvious.

We can fix this many ways.  We can forget the whole "combinde a rabit with the C and a" idea.  We can add "Drellowmar Systems" on the card apart from the logo (that way if they don't "get it" they can still read it.)

The Rabbit itself is quite obviously scanned from a hand drawing.  That might not be a bad thing, but combine that with the entire logo, and it is too cheap looking.

Target Market(s)

Technical folks. Investors. Business contacts.

Industry/Entity Type

Software

Requirements
Must have
• We have to clean up the logo, or replace it with something that hints at the same sort of things. (See the upload) Basically and innocent white bunny. Something that works on a Business Card.

All the information below:

Dorian Pell
ph (555) 314-9072
pell.dorian@mailvora.net
dorian@drellowmar.net
Nice to have
• I would like it to be serious, yet whimsical. An inside joke, so you get it if you know Quimby Larkets. But otherwise, it looks reasonably serious if you don't know Quimby Larkets.

I don't want it to be scary. (oddly, that my own efforts seem to make that easy to do)

Would like a set of colors that remind one of a cave, a rabbit, knights.... Not sure what those are...

```html
<!DOCTYPE html>
<html lang="en">
<head>
<meta charset="utf-8">
<title>Drellowmar – Dorian Pell Business Card</title>
<link rel="stylesheet" href="https://fonts.googleapis.com/css2?family=Open+Sans:ital,wght@0,400;0,700;1,700&family=PT+Sans+Narrow:wght@400&display=swap">
<style>
  :root {
    --brand-red: #c1202e;
    --brand-orange: #f07e1f;
    --brand-orange-light: #f59a2a;
    --ink: #444447;
    --ink-soft: #55565a;
    --paper-light: #ffffff;
    --paper-shade: #cfcfcf;
  }
  html, body {
    margin: 0;
    padding: 0;
    width: 1200px;
    height: 757px;
    overflow: hidden;
    background: #ffffff;
  }
  .card {
    position: relative;
    width: 1200px;
    height: 757px;
    overflow: hidden;
    background: radial-gradient(ellipse 900px 700px at 320px 260px, var(--paper-light) 0%, #f1f1f1 45%, var(--paper-shade) 100%);
    font-family: "PT Sans Narrow", "Arial Narrow", sans-serif;
  }
  .card__top-rule {
    position: absolute;
    top: 0; left: 0;
    width: 100%;
    height: 9px;
    background: var(--brand-red);
  }
  .card__band {
    position: absolute;
    left: 0; top: 0;
    width: 1200px;
    height: 757px;
  }
  .brand {
    position: absolute;
    left: 78px;
    top: 150px;
    display: flex;
    align-items: center;
    gap: 16px;
  }
  .brand__dot {
    width: 26px;
    height: 26px;
    border-radius: 50%;
    background: var(--brand-red);
  }
  .brand__name {
    font-family: "Open Sans", Arial, sans-serif;
    font-weight: 400;
    font-size: 64px;
    line-height: 1;
    color: var(--brand-red);
    letter-spacing: -0.5px;
  }
  .person {
    position: absolute;
    right: 84px;
    top: 138px;
    text-align: right;
    font-family: "Open Sans", Arial, sans-serif;
  }
  .person__name {
    margin: 0;
    font-size: 59px;
    font-weight: 700;
    line-height: 1.05;
    color: var(--brand-red);
    letter-spacing: -0.5px;
  }
  .person__title {
    margin: 0;
    font-size: 42px;
    font-weight: 400;
    line-height: 1.1;
    color: var(--ink);
  }
  .contacts {
    position: absolute;
    left: 94px;
    top: 290px;
    margin: 0;
    padding: 0;
    list-style: none;
  }
  .contacts__item {
    display: flex;
    align-items: center;
    height: 59.5px;
    font-size: 42px;
    color: var(--ink);
  }
  .contacts__icon {
    width: 44px;
    height: 44px;
    margin-right: 35px;
    fill: var(--ink);
    flex: none;
  }
  .slogan {
    position: absolute;
    right: 84px;
    bottom: 50px;
    margin: 0;
    font-family: "Open Sans", Arial, sans-serif;
    font-weight: 700;
    font-style: italic;
    font-size: 26px;
    color: var(--ink-soft);
  }
</style>
</head>
<body>
<main class="card">
  <div class="card__top-rule"></div>

  <svg class="card__band" viewBox="0 0 1200 757" role="img" aria-label="Decorative red and orange band along the lower edge">
    <defs>
      <linearGradient id="bandFill" x1="0" y1="0" x2="1" y2="0">
        <stop offset="0" stop-color="var(--brand-red)"/>
        <stop offset="0.45" stop-color="var(--brand-orange)"/>
        <stop offset="1" stop-color="var(--brand-orange-light)"/>
      </linearGradient>
    </defs>
    <path d="M0 680 Q 640 720 1200 480 L1200 757 L0 757 Z" fill="url(#bandFill)"/>
  </svg>

  <div class="brand">
    <span class="brand__dot"></span>
    <span class="brand__name">Drellowmar</span>
  </div>

  <header class="person">
    <h1 class="person__name">Dorian Pell</h1>
    <p class="person__title">Director</p>
  </header>

  <ul class="contacts">
    <li class="contacts__item">
      <svg class="contacts__icon" viewBox="0 0 24 24"><path d="M6.6 3.2 9 5.6c.5.5.5 1.2.1 1.7L7.8 8.8c.9 2.4 3 4.5 5.4 5.4l1.5-1.3c.5-.4 1.2-.4 1.7.1l2.4 2.4c.5.5.5 1.3 0 1.8l-1.5 1.5c-.8.8-2 1-3 .6C8.9 17.4 6.6 15.1 4.8 9.7c-.4-1-.2-2.2.6-3L6.6 3.2z" transform="translate(1 0)"/></svg>
      <span>(555) 314-9072</span>
    </li>
    <li class="contacts__item">
      <svg class="contacts__icon" viewBox="0 0 24 24"><rect x="7" y="3" width="10" height="5"/><rect x="3" y="9" width="18" height="8" rx="1.5"/><rect x="7" y="14" width="10" height="7" fill="#fff" stroke="var(--ink)" stroke-width="1.6"/><circle cx="18" cy="11.5" r="0.9" fill="#fff"/></svg>
      <span>(555) 314-9072</span>
    </li>
    <li class="contacts__item">
      <svg class="contacts__icon" viewBox="0 0 24 24"><rect x="6.5" y="1.5" width="11" height="21" rx="2"/><rect x="8.5" y="4" width="7" height="5" fill="#fff"/><g fill="#fff"><rect x="8.5" y="11" width="1.8" height="1.5"/><rect x="11.1" y="11" width="1.8" height="1.5"/><rect x="13.7" y="11" width="1.8" height="1.5"/><rect x="8.5" y="14" width="1.8" height="1.5"/><rect x="11.1" y="14" width="1.8" height="1.5"/><rect x="13.7" y="14" width="1.8" height="1.5"/><rect x="8.5" y="17" width="1.8" height="1.5"/><rect x="11.1" y="17" width="1.8" height="1.5"/><rect x="13.7" y="17" width="1.8" height="1.5"/></g></svg>
      <span>(555) 314-9072</span>
    </li>
    <li class="contacts__item">
      <svg class="contacts__icon" viewBox="0 0 24 24"><path d="M2 6h20v12H2z"/><path d="M2 6l10 7 10-7M2 18l7.5-6.5M22 18l-7.5-6.5" fill="none" stroke="#fff" stroke-width="1.4"/></svg>
      <span>pell.dorian@mailvora.net, dorian@drellowmar.net</span>
    </li>
    <li class="contacts__item">
      <svg class="contacts__icon" viewBox="0 0 24 24"><circle cx="12" cy="12" r="10"/><g fill="none" stroke="#fff" stroke-width="1.3"><ellipse cx="12" cy="12" rx="4.5" ry="10"/><path d="M2 12h20M4 7h16M4 17h16"/></g></svg>
      <span>www.drellowmar.net</span>
    </li>
  </ul>

  <p class="slogan">Your Slogan goes here!</p>
</main>
</body>
</html>
```